Power Point Showing our WHY: R4V

This PowerPoint design project aims to humanize critical educational statistics by transforming data into a powerful visual narrative. The goal is to put a face to the data, making abstract percentages more tangible and emotionally resonant for audiences.

The presentation begins with a single, impactful visual: 100 K–12 students, diverse in race and ethnicity, representing the full spectrum of learners across America.

Slide Progression & Visual Design:
Slide 1: "The Starting Line – 100 Students"
A visual display of 100 illustrated or photographic K–12 students.
Representation includes diversity in race, ethnicity, gender, and clothing to reflect real classrooms.
This slide sets the stage: every student matters.
Slide 2: "The First Drop – High School Graduation"
20 students fade away, showing the stark reality that only 80% graduate from high school.
Remaining 80 students stay on screen, reinforcing the message: not all students make it to the finish line.
Slide 3: "College Completion – A Narrowing Path"
From the 80 remaining students, another 35 fade away, illustrating that only 56% of students earn a college degree.
This leaves 45 students visible, showing the significant drop-off even after high school graduation.
Slide 4: "Low-Income Learners – The Equity Gap"
The image resets to the original 100 students.
This time, 87 students fade away, leaving only 13 standing, representing the 13% of low-income students who earn a college degree.
The emotional impact is amplified by the dramatic reduction in students who overcome economic barriers.
Design Notes:
Use consistent character illustrations or silhouettes for cohesion.
Employ subtle animations for "fading out" to enhance storytelling.
Slides should have minimal text—statistics should be overlaid in bold, clean typography.
Backgrounds should remain neutral or slightly muted to keep the focus on the students.
I am including out template to use

```html
<!DOCTYPE html>
<html lang="en">
<head>
<meta charset="utf-8">
<title>R4V – Showing our Why</title>
<link href="https://fonts.googleapis.com/css2?family=Montserrat:wght@500;700&display=swap" rel="stylesheet">
<style>
  :root{
    --stage:#6a6a6a;
    --paper:#ffffff;
    --ink:#111111;
    --navy:#032d3a;
    --magenta:#b0185a;
    --brand-text:#ffffff;
    --t-green:#9ccc6a;
    --t-orange:#f2894a;
    --t-blue:#7ec4e6;
    --t-red:#e8546a;
    --t-yellow:#f5c542;
    --t-purple:#a98bd9;
    --t-teal:#6fd1c4;
    --t-gray:#d9d6d0;
  }
  *{box-sizing:border-box;margin:0;padding:0}
  html,body{width:1200px;height:1200px;overflow:hidden}
  body{background:var(--stage);font-family:"Montserrat",sans-serif;position:relative}
  .slide{position:absolute;width:516px;height:290px;background:var(--paper);overflow:hidden}
  .col-left{left:62px}.col-right{left:621px}
  .row-1{top:112px}.row-2{top:454px}.row-3{top:802px}
  .portrait-grid{position:absolute;inset:0;display:grid;grid-template-columns:repeat(14,1fr);grid-template-rows:repeat(8,1fr)}
  .portrait-grid i{display:block}
  .a{background:var(--t-green)}.b{background:var(--t-orange)}.c{background:var(--t-blue)}
  .d{background:var(--t-red)}.e{background:var(--t-yellow)}.f{background:var(--t-purple)}
  .g{background:var(--t-teal)}.h{background:var(--t-gray)}.x{background:transparent}
  .caption{grid-column:1/8;grid-row:5/7;background:var(--paper);display:flex;flex-direction:column;justify-content:center;padding-left:30px;color:var(--ink);line-height:1.3}
  .caption .title{font-weight:700;font-size:17px}
  .caption .subtitle{font-weight:500;font-size:17px}
  .brand-slide{background:var(--navy);display:flex;align-items:center;justify-content:center;padding-bottom:20px}
  .brand-slide::after{content:"";position:absolute;left:0;right:0;bottom:0;height:6px;background:var(--magenta)}
  .brand-name{font-weight:700;font-size:40px;color:var(--brand-text);letter-spacing:1px}
</style>
</head>
<body>

<section class="slide col-left row-1">
  <div class="portrait-grid" role="img" aria-label="Grid of 100 diverse student portrait photos on colourful backgrounds">
    <i class="a"></i><i class="d"></i><i class="c"></i><i class="d"></i><i class="f"></i><i class="c"></i><i class="e"></i><i class="g"></i><i class="f"></i><i class="d"></i><i class="e"></i><i class="e"></i><i class="g"></i><i class="d"></i>
    <i class="b"></i><i class="b"></i><i class="d"></i><i class="b"></i><i class="h"></i><i class="b"></i><i class="c"></i><i class="b"></i><i class="b"></i><i class="f"></i><i class="b"></i><i class="a"></i><i class="b"></i><i class="d"></i>
    <i class="e"></i><i class="b"></i><i class="h"></i><i class="c"></i><i class="d"></i><i class="b"></i><i class="c"></i><i class="f"></i><i class="h"></i><i class="d"></i><i class="e"></i><i class="e"></i><i class="h"></i><i class="d"></i>
    <i class="b"></i><i class="h"></i><i class="e"></i><i class="c"></i><i class="d"></i><i class="d"></i><i class="h"></i><i class="d"></i><i class="c"></i><i class="d"></i><i class="b"></i><i class="d"></i><i class="h"></i><i class="b"></i>
    <div class="caption"><span class="title">The Starting Line</span><span class="subtitle">100 Students</span></div>
    <i class="h"></i><i class="e"></i><i class="b"></i><i class="g"></i><i class="d"></i><i class="g"></i><i class="c"></i>
    <i class="e"></i><i class="b"></i><i class="c"></i><i class="h"></i><i class="g"></i><i class="c"></i><i class="f"></i>
    <i class="f"></i><i class="h"></i><i class="g"></i><i class="e"></i><i class="d"></i><i class="h"></i><i class="c"></i><i class="e"></i><i class="h"></i><i class="d"></i><i class="g"></i><i class="h"></i><i class="e"></i><i class="f"></i>
    <i class="h"></i><i class="h"></i><i class="b"></i><i class="h"></i><i class="c"></i><i class="e"></i><i class="f"></i><i class="h"></i><i class="h"></i><i class="c"></i><i class="d"></i><i class="c"></i><i class="h"></i><i class="d"></i>
  </div>
</section>

<section class="slide col-right row-1">
  <div class="portrait-grid" role="img" aria-label="Grid of 100 diverse student portrait photos on colourful backgrounds">
    <i class="a"></i><i class="d"></i><i class="c"></i><i class="d"></i><i class="f"></i><i class="c"></i><i class="e"></i><i class="g"></i><i class="f"></i><i class="d"></i><i class="e"></i><i class="e"></i><i class="g"></i><i class="d"></i>
    <i class="b"></i><i class="b"></i><i class="d"></i><i class="b"></i><i class="h"></i><i class="b"></i><i class="c"></i><i class="b"></i><i class="b"></i><i class="f"></i><i class="b"></i><i class="a"></i><i class="b"></i><i class="d"></i>
    <i class="e"></i><i class="b"></i><i class="h"></i><i class="c"></i><i class="d"></i><i class="b"></i><i class="c"></i><i class="f"></i><i class="h"></i><i class="d"></i><i class="e"></i><i class="e"></i><i class="h"></i><i class="d"></i>
    <i class="b"></i><i class="h"></i><i class="e"></i><i class="c"></i><i class="d"></i><i class="d"></i><i class="h"></i><i class="d"></i><i class="c"></i><i class="d"></i><i class="b"></i><i class="d"></i><i class="h"></i><i class="b"></i>
    <div class="caption"><span class="title">Low-Income Learners</span><span class="subtitle">The Equity Gap</span></div>
    <i class="h"></i><i class="e"></i><i class="b"></i><i class="g"></i><i class="d"></i><i class="g"></i><i class="c"></i>
    <i class="e"></i><i class="b"></i><i class="c"></i><i class="h"></i><i class="g"></i><i class="c"></i><i class="f"></i>
    <i class="f"></i><i class="h"></i><i class="g"></i><i class="e"></i><i class="d"></i><i class="h"></i><i class="c"></i><i class="e"></i><i class="h"></i><i class="d"></i><i class="g"></i><i class="h"></i><i class="e"></i><i class="f"></i>
    <i class="h"></i><i class="h"></i><i class="b"></i><i class="h"></i><i class="c"></i><i class="e"></i><i class="f"></i><i class="h"></i><i class="h"></i><i class="c"></i><i class="d"></i><i class="c"></i><i class="h"></i><i class="d"></i>
  </div>
</section>

<section class="slide col-left row-2">
  <div class="portrait-grid" role="img" aria-label="Grid of 80 remaining student portrait photos with 20 gaps">
    <i class="a"></i><i class="d"></i><i class="c"></i><i class="d"></i><i class="f"></i><i class="x"></i><i class="e"></i><i class="g"></i><i class="f"></i><i class="x"></i><i class="e"></i><i class="x"></i><i class="g"></i><i class="d"></i>
    <i class="b"></i><i class="x"></i><i class="x"></i><i class="b"></i><i class="h"></i><i class="b"></i><i class="x"></i><i class="b"></i><i class="b"></i><i class="f"></i><i class="b"></i><i class="a"></i><i class="b"></i><i class="d"></i>
    <i class="e"></i><i class="x"></i><i class="h"></i><i class="c"></i><i class="d"></i><i class="b"></i><i class="c"></i><i class="f"></i><i class="h"></i><i class="d"></i><i class="x"></i><i class="e"></i><i class="x"></i><i class="d"></i>
    <i class="x"></i><i class="h"></i><i class="e"></i><i class="c"></i><i class="d"></i><i class="x"></i><i class="h"></i><i class="d"></i><i class="c"></i><i class="d"></i><i class="b"></i><i class="x"></i><i class="h"></i><i class="b"></i>
    <div class="caption"><span class="title">The First Drop</span><span class="subtitle">High School Graduation</span></div>
    <i class="h"></i><i class="e"></i><i class="b"></i><i class="g"></i><i class="d"></i><i class="g"></i><i class="x"></i>
    <i class="e"></i><i class="b"></i><i class="c"></i><i class="h"></i><i class="x"></i><i class="c"></i><i class="f"></i>
    <i class="f"></i><i class="x"></i><i class="g"></i><i class="e"></i><i class="d"></i><i class="h"></i><i class="c"></i><i class="e"></i><i class="x"></i><i class="d"></i><i class="g"></i><i class="h"></i><i class="e"></i><i class="x"></i>
    <i class="h"></i><i class="h"></i><i class="b"></i><i class="x"></i><i class="c"></i><i class="x"></i><i class="f"></i><i class="h"></i><i class="h"></i><i class="c"></i><i class="d"></i><i class="c"></i><i class="x"></i><i class="d"></i>
  </div>
</section>

<section class="slide col-right row-2">
  <div class="portrait-grid" role="img" aria-label="Mostly empty grid with 13 remaining student portrait photos">
    <i class="x"></i><i class="x"></i><i class="x"></i><i class="d"></i><i class="x"></i><i class="x"></i><i class="x"></i><i class="c"></i><i class="x"></i><i class="e"></i><i class="x"></i><i class="x"></i><i class="x"></i><i class="x"></i>
    <i class="x"></i><i class="x"></i><i class="x"></i><i class="x"></i><i class="x"></i><i class="x"></i><i class="x"></i><i class="x"></i><i class="x"></i><i class="x"></i><i class="x"></i><i class="x"></i><i class="x"></i><i class="x"></i>
    <i class="x"></i><i class="b"></i><i class="x"></i><i class="x"></i><i class="x"></i><i class="d"></i><i class="x"></i><i class="x"></i><i class="x"></i><i class="x"></i><i class="e"></i><i class="x"></i><i class="h"></i><i class="x"></i>
    <i class="x"></i><i class="x"></i><i class="e"></i><i class="x"></i><i class="x"></i><i class="x"></i><i class="x"></i><i class="x"></i><i class="x"></i><i class="x"></i><i class="x"></i><i class="x"></i><i class="x"></i><i class="x"></i>
    <div class="caption"><span class="title">Low-Income Learners</span><span class="subtitle">The Equity Gap</span></div>
    <i class="x"></i><i class="b"></i><i class="x"></i><i class="x"></i><i class="x"></i><i class="x"></i><i class="x"></i>
    <i class="e"></i><i class="x"></i><i class="x"></i><i class="x"></i><i class="g"></i><i class="x"></i><i class="f"></i>
    <i class="x"></i><i class="x"></i><i class="x"></i><i class="x"></i><i class="x"></i><i class="x"></i><i class="x"></i><i class="x"></i><i class="x"></i><i class="x"></i><i class="x"></i><i class="x"></i><i class="x"></i><i class="x"></i>
    <i class="x"></i><i class="x"></i><i class="x"></i><i class="x"></i><i class="x"></i><i class="x"></i><i class="x"></i><i class="x"></i><i class="x"></i><i class="x"></i><i class="x"></i><i class="c"></i><i class="x"></i><i class="x"></i>
  </div>
</section>

<section class="slide col-left row-3">
  <div class="portrait-grid" role="img" aria-label="Sparse grid with 45 remaining student portrait photos">
    <i class="x"></i><i class="d"></i><i class="c"></i><i class="d"></i><i class="f"></i><i class="x"></i><i class="e"></i><i class="x"></i><i class="f"></i><i class="x"></i><i class="e"></i><i class="x"></i><i class="g"></i><i class="x"></i>
    <i class="b"></i><i class="x"></i><i class="x"></i><i class="b"></i><i class="h"></i><i class="x"></i><i class="x"></i><i class="x"></i><i class="b"></i><i class="x"></i><i class="b"></i><i class="x"></i><i class="x"></i><i class="d"></i>
    <i class="x"></i><i class="x"></i><i class="x"></i><i class="x"></i><i class="x"></i><i class="b"></i><i class="x"></i><i class="x"></i><i class="x"></i><i class="h"></i><i class="e"></i><i class="x"></i><i class="x"></i><i class="x"></i>
    <i class="x"></i><i class="h"></i><i class="x"></i><i class="c"></i><i class="d"></i><i class="x"></i><i class="x"></i><i class="d"></i><i class="x"></i><i class="x"></i><i class="x"></i><i class="x"></i><i class="h"></i><i class="b"></i>
    <div class="caption"><span class="title">College Completion</span><span class="subtitle">A Narrowing Path</span></div>
    <i class="x"></i><i class="e"></i><i class="b"></i><i class="g"></i><i class="d"></i><i class="x"></i><i class="x"></i>
    <i class="e"></i><i class="x"></i><i class="c"></i><i class="x"></i><i class="g"></i><i class="c"></i><i class="x"></i>
    <i class="x"></i><i class="x"></i><i class="g"></i><i class="e"></i><i class="x"></i><i class="h"></i><i class="x"></i><i class="e"></i><i class="x"></i><i class="d"></i><i class="g"></i><i class="x"></i><i class="x"></i><i class="f"></i>
    <i class="h"></i><i class="x"></i><i class="b"></i><i class="x"></i><i class="x"></i><i class="x"></i><i class="x"></i><i class="f"></i><i class="x"></i><i class="x"></i><i class="x"></i><i class="x"></i><i class="x"></i><i class="d"></i>
  </div>
</section>

<section class="slide col-right row-3 brand-slide">
  <span class="brand-name">R4V</span>
</section>

</body>
</html>
```